Business Card Design

An energy company designed around renewable energy and energy storage that focuses on providing its energy at points on the grid that reduce costs and add value to the system.

Industry/Entity Type

Business

Contact Information for Business Card

Martin Dellacroix
Executive Vice President
41 K ST NE
Washington, DC 20017
240-555-0187
mdellacroix@brightvaleenergy.example

```html
<!DOCTYPE html>
<html lang="en">
<head>
<meta charset="utf-8">
<title>Business Card – Martin Dellacroix</title>
<link rel="stylesheet" href="https://fonts.googleapis.com/css2?family=Lato:wght@400;700&display=swap">
<style>
  :root {
    --backdrop: #2b2724;
    --card: #1c1c1d;
    --card-back: #161617;
    --orange: #f57c14;
    --white: #f4f4f4;
    --silver: #b9b9b9;
    --rule: #3c3c3e;
  }
  * { box-sizing: border-box; margin: 0; padding: 0; }
  html, body {
    width: 1200px; height: 844px; overflow: hidden;
    background: var(--backdrop);
    font-family: "Lato", sans-serif;
  }
  .stage {
    position: relative; width: 1200px; height: 844px;
    display: flex; align-items: center; justify-content: center; gap: 60px;
  }
  .card {
    width: 520px; height: 298px; position: relative;
    border-radius: 4px;
    box-shadow: 0 10px 30px rgba(0,0,0,.45);
  }
  .card-front { background: var(--card); }
  .card-back {
    background: var(--card-back);
    display: flex; align-items: center; justify-content: center;
  }

  /* brand block */
  .brand {
    position: absolute; left: 44px; top: 46px;
    display: flex; align-items: center; gap: 20px;
  }
  .brand-mark { width: 58px; height: 58px; background: var(--orange); }
  .brand-rule { width: 1px; height: 74px; background: var(--rule); }
  .brand-name {
    font-weight: 700; font-size: 22px; line-height: 1.15;
    letter-spacing: 1px; text-transform: uppercase; color: var(--white);
  }

  /* identity, bottom left */
  .identity {
    position: absolute; left: 20px; top: 166px; width: 196px;
    text-align: right; color: var(--white);
  }
  .identity-name { font-size: 20px; font-weight: 400; white-space: nowrap; }
  .identity-role { font-size: 13px; color: var(--orange); margin: 2px 0 10px; white-space: nowrap; }
  .identity-address { font-size: 13px; line-height: 1.35; white-space: nowrap; }

  .split-rule {
    position: absolute; left: 232px; top: 146px;
    width: 1px; height: 124px; background: var(--rule);
  }

  /* contact list */
  .contacts {
    position: absolute; left: 248px; top: 164px;
    list-style: none; color: var(--white); font-size: 12px;
  }
  .contacts li { display: flex; align-items: center; gap: 9px; height: 27px; white-space: nowrap; }
  .contact-icon {
    width: 16px; height: 16px; background: var(--orange); border-radius: 2px;
    display: flex; align-items: center; justify-content: center; flex: none;
  }
  .contact-icon svg { width: 11px; height: 11px; }

  .back-name {
    font-weight: 700; font-size: 30px; letter-spacing: 2px;
    text-transform: uppercase; color: var(--silver); text-align: center; line-height: 1.2;
  }
</style>
</head>
<body>
<main class="stage">
  <section class="card card-front" aria-label="Business card front">
    <div class="brand">
      <div class="brand-mark"></div>
      <div class="brand-rule"></div>
      <div class="brand-name">Brightvale<br>Energy</div>
    </div>

    <div class="identity">
      <p class="identity-name">Martin Dellacroix</p>
      <p class="identity-role">Executive Vice President</p>
      <p class="identity-address">41 K ST NE<br>Washington, DC 20017</p>
    </div>

    <div class="split-rule"></div>

    <ul class="contacts">
      <li>
        <span class="contact-icon"><svg viewBox="0 0 12 12"><path d="M3 1 L5 3.5 L4 4.8 Q5.2 7 7.2 8 L8.5 7 L11 9 L10 11 Q5 11 1 6 Q1 3 3 1Z" fill="#fff"/></svg></span>
        240-555-0187
      </li>
      <li>
        <span class="contact-icon"><svg viewBox="0 0 12 12"><rect x="1" y="2.5" width="10" height="7" fill="#fff"/><path d="M1 2.5 L6 7 L11 2.5" stroke="#f57c14" stroke-width="1" fill="none"/></svg></span>
        mdellacroix@brightvaleenergy.example
      </li>
      <li>
        <span class="contact-icon"><svg viewBox="0 0 12 12"><circle cx="6" cy="6" r="4.5" stroke="#fff" stroke-width="1.3" fill="none"/><path d="M1.5 6 H10.5 M6 1.5 Q3.5 6 6 10.5 M6 1.5 Q8.5 6 6 10.5" stroke="#fff" stroke-width="1" fill="none"/></svg></span>
        brightvaleenergy.example
      </li>
    </ul>
  </section>

  <section class="card card-back" aria-label="Business card back">
    <p class="back-name">Brightvale<br>Energy</p>
  </section>
</main>
</body>
</html>
```